I already have a logo created by Quillory Makers that I'm very happy with. I need to spruce up my business card now. Its a double sided card with not much info on it, I like to keep it simple.
Front of card: name, phone # email address, web address. Tag Line "Outsourced Technology Solutions", under that it says Business Voice Services & Electronic Protection.
Rear of Card: Content written inside a "cloud" saying "Cloud Solutions" "Cloud Integrity"

Target Market(s)

Business to Business

Industry/Entity Type

Business

Contact Information for Business Card

We are in the technology field. Providing Telephone systems (hardware), SIP Trunks (dial tone/local/long distance/telephone #'s), LAN (Local Area Network)infrastructure cabling, Data Center solutions and Security Applications (Camera systems, Access Control systems,

Requirements
Must have
• Must have brevity
Should not have
• Clutter and/or too much information

```html
<!DOCTYPE html>
<html lang="en">
<head>
<meta charset="utf-8">
<title>Northvale Connect Systems – Business Card</title>
<link rel="stylesheet" href="https://fonts.googleapis.com/css2?family=Raleway:wght@500;700&family=Roboto:wght@400;500&display=swap">
<style>
  :root {
    --navy: #1f3f8c;
    --blue-dark: #254a9c;
    --blue-light: #5a84cc;
    --grey-text: #8a8f99;
    --rule: #9aa0a8;
    --lavender: #e9e9f3;
    --paper: #ffffff;
    --backdrop: #e4e5e8;
  }
  * { box-sizing: border-box; margin: 0; padding: 0; }
  html, body { width: 1200px; height: 800px; overflow: hidden; }
  body {
    background: var(--backdrop);
    font-family: "Roboto", Arial, sans-serif;
    position: relative;
  }
  .card {
    position: absolute;
    top: 245px;
    width: 540px;
    height: 310px;
    border-radius: 4px;
    overflow: hidden;
    box-shadow: 0 6px 18px rgba(0,0,0,0.12);
  }
  .card-front { left: 40px; background: var(--paper); }
  .card-back {
    left: 620px;
    background: linear-gradient(135deg, var(--blue-dark) 0%, var(--blue-light) 100%);
  }

  /* Front */
  .brand { position: absolute; left: 36px; top: 34px; }
  .brand-name {
    display: flex; align-items: center; gap: 10px;
    font-family: "Raleway", Arial, sans-serif;
    font-weight: 700; font-size: 22px; color: var(--navy);
    white-space: nowrap;
  }
  .brand-mark { width: 14px; height: 14px; background: var(--navy); flex: none; }
  .tagline {
    margin-top: 6px; padding-top: 5px;
    border-top: 1px solid var(--rule);
    font-family: "Raleway", Arial, sans-serif;
    font-weight: 500; font-size: 15px; color: var(--grey-text);
    white-space: nowrap;
  }
  .services {
    margin-top: 3px;
    font-family: "Raleway", Arial, sans-serif;
    font-size: 10px; color: var(--grey-text);
    white-space: nowrap;
  }
  .person { position: absolute; left: 36px; top: 130px; }
  .person-name { font-family: "Raleway", Arial, sans-serif; font-weight: 700; font-size: 20px; color: var(--navy); }
  .person-title { font-size: 12px; color: var(--grey-text); margin-top: 2px; }
  .divider {
    position: absolute; left: 36px; right: 0; top: 182px;
    border-top: 1px solid var(--rule);
  }
  .contact { position: absolute; left: 36px; top: 192px; list-style: none; }
  .contact li {
    display: flex; align-items: center; gap: 8px;
    font-size: 12px; color: var(--navy); line-height: 19px;
  }
  .contact svg { width: 12px; height: 12px; }
  .decor-panel {
    position: absolute; right: 0; bottom: 0;
    width: 300px; height: 120px;
    background: linear-gradient(120deg, rgba(233,233,243,0) 0%, var(--lavender) 60%);
  }
  .address {
    position: absolute; right: 30px; bottom: 26px;
    text-align: right; font-size: 13px; color: var(--navy); line-height: 18px;
    border-top: 1px solid var(--rule); padding-top: 6px; width: 200px;
    font-style: normal;
  }

  /* Back */
  .cloud { position: absolute; inset: 0; width: 540px; height: 310px; }
  .back-brand {
    position: absolute; left: 150px; width: 280px; top: 72px; text-align: center;
  }
  .back-brand .brand-name { justify-content: center; font-size: 13px; gap: 6px; }
  .back-brand .brand-mark { width: 9px; height: 9px; }
  .back-brand .tagline { display: inline-block; font-size: 10px; margin-top: 3px; padding-top: 3px; }
  .back-brand .services { font-size: 7.5px; }
</style>
</head>
<body>

<section class="card card-front" aria-label="Card front">
  <div class="brand">
    <div class="brand-name"><span class="brand-mark"></span>Northvale Connect Systems, LLC</div>
    <div class="tagline">Outsourced Technology Solutions</div>
    <div class="services">Business Voice Services &amp; Electronic Protection</div>
  </div>

  <div class="person">
    <div class="person-name">Evan Marlow</div>
    <div class="person-title">Director Operations</div>
  </div>
  <div class="divider"></div>

  <ul class="contact">
    <li>
      <svg viewBox="0 0 12 12"><rect width="12" height="12" rx="2" fill="#8a8f99"/><path d="M4 3l1.2 1.6-.7.8c.5 1 1.2 1.7 2.1 2.1l.8-.7L9 8l-.6 1.2C6 9 3 6 2.8 3.6Z" fill="#fff"/></svg>
      555 014 2277
    </li>
    <li>
      <svg viewBox="0 0 12 12"><rect width="12" height="12" rx="2" fill="#8a8f99"/><rect x="2.5" y="3.5" width="7" height="5" fill="none" stroke="#fff"/><path d="M2.5 3.5 6 6.5l3.5-3" fill="none" stroke="#fff"/></svg>
      hello@northvaleconnect.com
    </li>
    <li>
      <svg viewBox="0 0 12 12"><rect width="12" height="12" rx="2" fill="#8a8f99"/><circle cx="6" cy="6" r="3.3" fill="none" stroke="#fff"/><path d="M2.7 6h6.6M6 2.7v6.6" stroke="#fff" stroke-width=".8"/></svg>
      www.northvaleconnect.com
    </li>
  </ul>

  <div class="decor-panel" role="img" aria-label="Faint angular background decoration"></div>

  <address class="address">418 Harbor Lane<br>Brookfield 20417</address>
</section>

<section class="card card-back" aria-label="Card back">
  <svg class="cloud" viewBox="0 0 540 310">
    <path d="M70,292 C20,292 15,210 60,195 C40,130 110,95 150,120 C170,20 420,10 430,90 C480,75 530,130 500,195 C530,210 525,292 470,292 Z"
          fill="#ffffff" stroke="#8fb0e6" stroke-width="3"/>
    <g stroke="#2b4f9e" stroke-width="1.2">
      <line x1="110" y1="150" x2="470" y2="150"/>
      <line x1="75"  y1="182" x2="490" y2="182"/>
      <line x1="50"  y1="214" x2="495" y2="214"/>
      <line x1="50"  y1="246" x2="495" y2="246"/>
    </g>
  </svg>
  <div class="back-brand">
    <div class="brand-name"><span class="brand-mark"></span>Northvale Connect Systems, LLC</div>
    <div class="tagline">Outsourced Technology Solutions</div>
    <div class="services">Business Voice Services &amp; Electronic Protection</div>
  </div>
</section>

</body>
</html>
```